English and Spanish Language School Needs a Business Card

Need a business card design a startup company called Corvelle Language School. The company will offer English and Spanish conversational level courses designed to make the learner feel comfortable with grammar and vocabulary. We would like to see a logo with some colour that should communicate learning, growth.

Target Market(s)

Consumers and businesses

Industry/Entity Type

Education

Contact Information for Business Card

TBD

Font styles to use
Serif

Requirements
Must have
• Include the following
• Logo
• Name
• Title
• Cellphone Number
• Office Phone number
• Email address
• Office Address

```html
<!DOCTYPE html>
<html lang="en">
<head>
<meta charset="utf-8">
<title>Corvelle Language School — Business Card</title>
<link rel="stylesheet" href="https://fonts.googleapis.com/css2?family=Tinos:wght@400;700&display=swap">
<style>
  :root {
    --brand-red: #c81e26;
    --card-white: #ffffff;
    --ink: #222222;
    --page: #ecebe8;
    --rule: #c81e26;
  }
  * { box-sizing: border-box; margin: 0; padding: 0; }
  html, body { width: 1200px; height: 900px; overflow: hidden; }
  body {
    background: var(--page);
    font-family: "Tinos", "Times New Roman", serif;
    position: relative;
  }
  .card {
    position: absolute;
    width: 560px;
    height: 320px;
    border-radius: 16px;
    box-shadow: 0 6px 18px rgba(0,0,0,0.18);
  }
  .card--back {
    left: 560px; top: 90px;
    background: var(--brand-red);
    color: var(--card-white);
  }
  .card--front {
    left: 80px; top: 490px;
    background: var(--card-white);
    color: var(--ink);
  }
  /* Back */
  .back-name {
    position: absolute;
    left: 0; right: 0; top: 110px;
    text-align: center;
    font-weight: 700;
    font-size: 64px;
    line-height: 1;
  }
  .back-tagline {
    position: absolute;
    left: 0; right: 0; top: 180px;
    text-align: center;
    font-weight: 700;
    font-size: 24px;
  }
  .back-web {
    position: absolute;
    left: 0; right: 0; bottom: 36px;
    text-align: center;
    font-size: 15px;
    letter-spacing: 0.5px;
  }
  /* Front */
  .front-logo {
    position: absolute;
    left: 34px; top: 60px;
    width: 230px;
    color: var(--brand-red);
    font-weight: 700;
  }
  .front-logo .logo-word { font-size: 48px; line-height: 1; display: block; }
  .front-logo .logo-sub { font-size: 19px; display: block; margin-top: 6px; }
  .divider {
    position: absolute;
    left: 272px; top: 40px;
    width: 1.5px; height: 240px;
    background: linear-gradient(to bottom, var(--rule), rgba(200,30,38,0));
  }
  .contact {
    position: absolute;
    left: 296px; top: 44px;
    font-size: 14px;
    line-height: 1.45;
  }
  .contact-name { color: var(--brand-red); font-size: 26px; line-height: 1.1; }
  .contact-title { font-size: 14px; font-weight: 700; margin-bottom: 10px; }
  .contact-address { margin-bottom: 8px; }
  .contact-list { list-style: none; }
  .contact-list li { display: flex; align-items: center; gap: 8px; }
  .contact-list svg { width: 14px; height: 14px; flex: none; }
</style>
</head>
<body>
  <section class="card card--back" aria-label="Card back">
    <div class="back-name">Corvelle</div>
    <div class="back-tagline">Language School</div>
    <div class="back-web">www.corvelleschool.com</div>
  </section>

  <section class="card card--front" aria-label="Card front">
    <div class="front-logo">
      <span class="logo-word">Corvelle</span>
      <span class="logo-sub">Language School</span>
    </div>
    <div class="divider"></div>
    <div class="contact">
      <div class="contact-name">Marcus Hale</div>
      <div class="contact-title">President</div>
      <div class="contact-address">742 Harlow Avenue, Suite 300<br>Brookfield, OR 97410</div>
      <ul class="contact-list">
        <li>
          <svg viewBox="0 0 16 16" aria-hidden="true"><path fill="#c81e26" d="M2 5c0-2 2-3 6-3s6 1 6 3v1h-3V4.8C10 4.3 9 4 8 4s-2 .3-3 .8V6H2zM4 7h8l1 7H3z"/><circle cx="8" cy="10.5" r="1.6" fill="#fff"/></svg>
          (503) 555-0142
        </li>
        <li>
          <svg viewBox="0 0 16 16" aria-hidden="true"><rect x="4" y="1" width="8" height="14" rx="1.5" fill="none" stroke="#c81e26" stroke-width="1.4"/><circle cx="8" cy="12.5" r="0.9" fill="#c81e26"/></svg>
          (503) 555-0187
        </li>
        <li>
          <svg viewBox="0 0 16 16" aria-hidden="true"><rect x="1" y="3" width="14" height="10" fill="#c81e26"/><path d="M1.5 3.5 8 9l6.5-5.5" fill="none" stroke="#fff" stroke-width="1.2"/></svg>
          hello@corvelleschool.com
        </li>
        <li>
          <svg viewBox="0 0 16 16" aria-hidden="true"><circle cx="8" cy="8" r="6.5" fill="#c81e26"/><path d="M1.5 8h13M8 1.5c-2.5 3-2.5 10 0 13M8 1.5c2.5 3 2.5 10 0 13M2.8 4.8h10.4M2.8 11.2h10.4" fill="none" stroke="#fff" stroke-width="0.8"/></svg>
          www.corvelleschool.com
        </li>
      </ul>
    </div>
  </section>
</body>
</html>
```